BLUE HAVEN (Business Card for Training Company)

Blue Haven is a training and consultancy company with a focus on executive protection and medical. I would like the card to be nice and sharp, not overdone and in black and red. I would also like it to highlight that it is "A Dravin Company"

I would like it to be simple and highlight a few things.

1. Name
2. Title
3. Phone Number
4. Email

I would also like www.dravinholdings.example/blue-haven to be on the card somewhere.

Target Market(s)

Security Companies

Industry/Entity Type

Security

Contact Information for Business Card

Blue Haven is a training and consultancy company with a focus on executive protection and medical. I would like the card to be nice and sharp, not overdone and in black and red. I would also like it to highlight that it is "A Dravin Company" I would like it to be simple and highlight a few things. 1. Name 2. Title 3. Phone Number 4. Email I would also like www.dravinholdings.example/blue-haven to be on the card somewhere.

Requirements
Must have
• A Dravin Company listed on the card and the website
Nice to have
• Highlight Medical Training, Consultancy & Executive Protection Courses

```html
<!DOCTYPE html>
<html lang="en">
<head>
<meta charset="utf-8">
<title>Blue Haven – Business Card</title>
<link href="https://fonts.googleapis.com/css2?family=Arimo:ital,wght@0,400;0,700;1,400&display=swap" rel="stylesheet">
<style>
  :root {
    --backdrop: #262626;
    --card: #1f1f1f;
    --card-light: #2e2e2e;
    --accent: #7a1518;
    --text: #ffffff;
    --text-soft: #e6e6e6;
  }
  * { box-sizing: border-box; margin: 0; padding: 0; }
  html, body {
    width: 1200px; height: 900px; overflow: hidden;
    background: var(--backdrop);
    font-family: "Arimo", Arial, sans-serif;
  }
  .stage {
    width: 1200px; height: 900px;
    display: flex; flex-direction: column;
    align-items: center; justify-content: center; gap: 40px;
  }
  .card {
    width: 700px; height: 400px;
    background: linear-gradient(120deg, var(--card) 0%, var(--card) 40%, var(--card-light) 100%);
    box-shadow: 0 6px 18px rgba(0,0,0,.55);
    position: relative;
    color: var(--text);
  }
  /* Back side */
  .card-back {
    display: flex; flex-direction: column;
    align-items: center; justify-content: center;
    text-align: center; font-weight: 700;
  }
  .parent-line { font-size: 30px; letter-spacing: 2px; }
  .cta { font-size: 22px; letter-spacing: 1.5px; margin-top: 10px; }
  .back-url { font-size: 28px; letter-spacing: 1px; margin-top: 6px; }

  /* Front side */
  .card-front { display: flex; align-items: center; padding: 0 0 0 60px; }
  .brand-name {
    width: 250px;
    font-size: 58px; font-weight: 700; line-height: 1;
    color: var(--text); letter-spacing: 1px;
  }
  .divider {
    width: 2px; height: 190px; background: var(--accent);
    margin: 0 24px 0 20px;
  }
  .contact { font-size: 17px; color: var(--text-soft); line-height: 1.25; }
  .person-name { font-size: 26px; font-weight: 700; color: var(--accent); text-transform: uppercase; }
  .person-title { font-style: italic; font-size: 17px; margin-bottom: 12px; }
  .address { margin-bottom: 8px; }
  .contact-row { display: flex; align-items: center; gap: 8px; margin-top: 3px; }
  .contact-row svg { width: 14px; height: 14px; flex: none; fill: var(--accent); }
</style>
</head>
<body>
<main class="stage">
  <section class="card card-back">
    <p class="parent-line">A DRAVIN COMPANY</p>
    <p class="cta">VISIT NOW</p>
    <p class="back-url">www.dravinholdings.example/blue-haven</p>
  </section>

  <section class="card card-front">
    <p class="brand-name">BLUE<br>HAVEN</p>
    <div class="divider"></div>
    <div class="contact">
      <p class="person-name">Daniel Reyes</p>
      <p class="person-title">CEO/Founder</p>
      <p class="address">48 Harbor Lane, Suite 210,<br>Portland, Maine 04101</p>
      <p class="contact-row">
        <svg viewBox="0 0 16 16" aria-hidden="true"><path d="M3 1h3l1.5 4-2 1.2a9 9 0 0 0 4.3 4.3L11 8.5l4 1.5v3a2 2 0 0 1-2 2A13 13 0 0 1 1 3a2 2 0 0 1 2-2z"/></svg>
        01987654320
      </p>
      <p class="contact-row">
        <svg viewBox="0 0 16 16" aria-hidden="true"><path d="M1 3h14v10H1z M1 3l7 6 7-6" stroke="#1f1f1f" stroke-width="1"/></svg>
        info@dravinholdings.example
      </p>
      <p class="contact-row">
        <svg viewBox="0 0 16 16" aria-hidden="true"><circle cx="8" cy="8" r="7"/><path d="M1 8h14M8 1c-3 3-3 11 0 14M8 1c3 3 3 11 0 14" stroke="#1f1f1f" stroke-width="1" fill="none"/></svg>
        www.dravinholdings.example/blue-haven
      </p>
    </div>
  </section>
</main>
</body>
</html>
```